Tampa Bay fishing guide needs stunning website.

I currently have a site - www.reelcoveguide.example which I personally put together using the Plixo platform and I am looking for a redesign on a different platform (Brindlepress?) that will allow me to easily create landing pages in the future. Would like to have a block for visitors to opt in to newsletter. Need social media links on all pages.
Updates

I would like to let my visitors know that I am able to handle their fishing charter needs here in the Tampa Bay area, if I'm not available for the dates they are looking to go I can refer them to a reputable captain in the area.

Target Market(s)

United States

Industry/Entity Type

Tourism

Coding

Coded - Design and coding required

Number of Pages Required

5+ page

Font styles to use
Sans Serif

Colors
0355a3
3176b5
85abd2
fbf289

Requirements
Must have
• Mobile Responsive, Ability to insert Vantor Metrics, Quillbook pixels, ability to add custom landing pages in future
Nice to have
• Clean, easy navigation

```html
<!DOCTYPE html>
<html lang="en">
<head>
<meta charset="utf-8">
<title>Capt. Dale Marlow Sport Fishing Charters</title>
<link href="https://fonts.googleapis.com/css2?family=Raleway:wght@400;500;600;700;800&family=Lato:wght@400;700&display=swap" rel="stylesheet">
<style>
:root{
  --blue-deep:#0355a3;
  --blue-mid:#3176b5;
  --blue-soft:#85abd2;
  --yellow:#fbf289;
  --ink:#222;
  --text:#444;
  --dark:#2b2b2b;
  --darker:#1e1e1e;
  --pale:#eef4f9;
  --white:#fff;
}
*{box-sizing:border-box;margin:0;padding:0}
html,body{width:1200px;height:3136px;overflow:hidden}
body{font-family:'Lato',sans-serif;color:var(--text);background:var(--white);position:relative}
.section{position:absolute;left:0;width:1200px}
.head-font{font-family:'Raleway',sans-serif}

/* top bar */
.topbar{top:0;height:30px;background:var(--blue-deep);color:#dfe9f5;font-size:11px}
.topbar .contact{position:absolute;left:163px;top:8px;display:flex;gap:26px}
.topbar .contact span{display:flex;align-items:center;gap:6px}
.topbar .social{position:absolute;right:163px;top:8px;display:flex;gap:12px}
.dot{width:13px;height:13px;border-radius:50%;background:#dfe9f5;display:inline-block}

/* header */
.header{top:30px;height:102px;background:var(--white);box-shadow:0 1px 3px rgba(0,0,0,.08)}
.brand{position:absolute;left:163px;top:30px;display:flex;align-items:center;gap:10px;font-family:'Raleway',sans-serif;font-weight:800;font-size:30px;color:var(--blue-mid)}
.brand .mark{width:22px;height:22px;border-radius:50%;background:var(--blue-mid)}
.nav{position:absolute;right:161px;top:42px;display:flex;gap:42px;font-family:'Raleway',sans-serif;font-size:13px;color:#333}
.nav a{color:inherit;text-decoration:none;padding-bottom:10px}
.nav a.active{color:var(--blue-deep);font-weight:700;border-bottom:2px solid var(--blue-deep)}

/* hero */
.hero{top:132px;height:510px;background:linear-gradient(180deg,#c9d3d6 0%,#8fa3a8 45%,#2f5a6a 75%,#1e4a5c 100%)}
.hero-text{position:absolute;left:0;width:1200px;top:230px;text-align:center;color:var(--white)}
.hero-text h1{font-family:'Raleway',sans-serif;font-weight:800;font-size:29px;letter-spacing:.3px;text-shadow:0 1px 3px rgba(0,0,0,.4)}
.hero-text p{font-family:'Raleway',sans-serif;font-size:23px;margin-top:8px;text-shadow:0 1px 3px rgba(0,0,0,.4)}
.slide-arrow{position:absolute;width:40px;height:40px;border-radius:50%;border:2px solid rgba(255,255,255,.8);top:250px;display:flex;align-items:center;justify-content:center}
.badge{position:absolute;left:859px;top:31px;width:151px;height:121px;background:var(--white);border-radius:8px;box-shadow:0 2px 6px rgba(0,0,0,.3);overflow:hidden}
.badge .bar{position:absolute;left:0;bottom:0;width:100%;height:26px;background:var(--blue-mid)}
.badge .shape{position:absolute;left:18px;top:18px;width:60px;height:10px;background:#d7dde3;border-radius:3px}
.badge .shape2{position:absolute;left:18px;top:38px;width:110px;height:8px;background:#e7eaee;border-radius:3px}
.badge .circle{position:absolute;right:18px;top:14px;width:22px;height:22px;border-radius:50%;background:#e0b84a}

/* bubble sections */
.bubbly{background:radial-gradient(circle at 20% 30%,#f6fafd 0,#e6eff7 60%,#dbe8f3 100%)}
.welcome{top:642px;height:324px;text-align:center}
.welcome h2{position:absolute;top:62px;left:0;width:1200px;font-family:'Raleway',sans-serif;font-weight:700;font-size:29px;color:var(--ink);display:flex;justify-content:center;align-items:center;gap:12px}
.welcome h2 .name{color:var(--blue-mid);font-weight:800;font-size:32px}
.rule{width:70px;height:3px;background:var(--blue-deep);margin:0 auto}
.welcome .rule{position:absolute;top:146px;left:565px}
.welcome p{position:absolute;top:168px;left:160px;width:880px;font-size:13.5px;line-height:27px;color:#333}
.btn{display:inline-block;background:var(--blue-deep);color:var(--white);font-family:'Raleway',sans-serif;font-weight:700;font-size:13px;padding:8px 19px;border-radius:2px}
.welcome .btn{position:absolute;top:258px;left:552px}

/* pickup + booking */
.booking{top:966px;height:497px;background:linear-gradient(120deg,#3c5566 0%,#52708a 40%,#6c8397 70%,#8d97a0 100%)}
.booking h3{position:absolute;top:38px;font-family:'Raleway',sans-serif;font-weight:700;font-size:29px;color:var(--white)}
.mini-arrows{position:absolute;left:526px;top:48px;display:flex;gap:5px}
.mini-arrows span{width:24px;height:24px;border-radius:50%;border:1px solid rgba(255,255,255,.8);display:flex;align-items:center;justify-content:center}
.place-card{position:absolute;left:163px;top:112px;width:422px;height:339px;background:var(--white);padding:10px 10px}
.place-card h4{font-family:'Raleway',sans-serif;font-weight:500;font-size:21px;color:#222}
.place-card .addr{font-size:13px;color:#333;margin-top:4px}
.place-card .photo{margin-top:14px;height:255px;background:linear-gradient(160deg,#1d6f93 0%,#3aa0bd 45%,#5e8f5a 60%,#2b84a8 100%)}
.form-card{position:absolute;left:619px;top:112px;width:420px;height:339px;background:var(--white);padding:24px 24px}
.form-grid{display:grid;grid-template-columns:1fr 1fr;column-gap:12px;row-gap:12px}
.field label{display:block;font-size:11px;font-weight:700;color:#222;margin-bottom:4px}
.field .input{height:27px;border:1px solid #cfcfcf;font-size:11px;color:#666;padding:6px 8px;display:flex;justify-content:space-between;align-items:center}
.field.full{grid-column:1/3}
.field .area{height:50px}
.form-card .btn{display:block;width:112px;margin:12px auto 0;text-align:center}

/* rates */
.rates{top:1463px;height:339px;background:var(--white)}
.sec-title{position:absolute;left:0;width:1200px;text-align:center;font-family:'Raleway',sans-serif;font-weight:700;font-size:29px;color:var(--ink)}
.sec-title em{font-style:normal;color:var(--blue-mid)}
.rates .sec-title{top:34px}
.rates .rule{position:absolute;top:86px;left:565px}
.rate{position:absolute;top:125px;display:flex;gap:17px}
.rate .photo{width:172px;height:178px}
.rate .info{width:236px}
.rate h4{font-family:'Raleway',sans-serif;font-weight:700;font-size:14.5px;line-height:22px;color:#222}
.rate p{font-size:11px;line-height:17px;color:#444;margin-top:8px}
.rate .btn{margin-top:12px;font-size:11px;padding:7px 16px}
.side-arrow{position:absolute;top:186px;width:36px;height:36px;border-radius:50%;border:1px solid #999;display:flex;align-items:center;justify-content:center}

/* gallery */
.gallery{top:1802px;height:564px;background:linear-gradient(110deg,#cfd4d6 0%,#a7b3b9 30%,#6f848e 60%,#8a969c 100%)}
.gallery .sec-title{top:24px}
.gallery .rule{position:absolute;top:76px;left:565px}
.tile{position:absolute;width:203px;background:#dcdcdc;box-shadow:0 1px 3px rgba(0,0,0,.3)}
.tile .pin{position:absolute;left:0;top:0;width:203px;height:28px}
.tile .shot{position:absolute;left:6px;top:30px;right:6px;bottom:6px}

/* testimonials */
.testimonials{top:2366px;height:362px}
.testimonials .sec-title{top:43px}
.testimonials .rule{position:absolute;top:96px;left:565px}
.quote{position:absolute;top:114px;left:290px;width:620px;text-align:center;font-size:12px;line-height:21px;color:#555}
.qmark{position:absolute;top:92px;font-family:Georgia,serif;font-size:96px;color:#d4d9de;line-height:1}
.client-name{position:absolute;top:198px;left:0;width:1200px;text-align:center;font-family:'Raleway',sans-serif;font-weight:700;font-size:14px;color:var(--blue-deep)}
.avatar{position:absolute;top:236px;width:78px;height:78px;border-radius:50%;border:3px solid var(--white);box-shadow:0 1px 4px rgba(0,0,0,.25);background:linear-gradient(180deg,#c8b8a6,#8a7464)}
.avatar.current{border-color:var(--blue-soft)}

/* footer */
.footer{top:2728px;height:276px;background:var(--dark);color:#ccc}
.fcol{position:absolute;top:50px}
.fcol h5{font-family:'Raleway',sans-serif;font-weight:500;font-size:16px;color:#ddd;padding-bottom:10px;border-bottom:1px solid #444;width:170px}
.fcol ul{list-style:none;margin-top:12px}
.fcol li{font-size:11px;line-height:27px;color:#ccc}
.fcol li::before{content:"› ";color:#999}
.fcol li.on{color:var(--white);font-weight:700}
.fcontact p{font-size:12px;line-height:27px;display:flex;align-items:center;gap:10px;margin-top:4px}
.fsocial{display:flex;gap:16px;margin-top:14px}
.fsocial .dot{background:#ccc}
.plugin{position:absolute;left:811px;top:32px;width:228px;height:208px;background:var(--white);border:1px solid #3e5f9a}
.plugin .bar{height:28px;background:var(--blue-mid);display:flex;justify-content:space-between;align-items:center;padding:0 8px;color:var(--white);font-size:10px}
.plugin .bar b{font-size:11px}
.post{display:flex;gap:8px;padding:10px 8px 0}
.post .thumb{width:44px;height:36px;background:linear-gradient(135deg,#d9a25a,#7a5a3a);flex:none}
.post p{font-size:10px;line-height:14px;color:var(--blue-mid)}
.post small{display:block;font-size:8.5px;color:#888}
.plugin .foot{position:absolute;bottom:0;left:0;right:0;border-top:1px solid #ddd;font-size:9.5px;color:#3e5f9a;padding:6px 8px}

/* newsletter */
.newsletter{top:3004px;height:92px;background:var(--blue-mid)}
.nl-icon{position:absolute;left:183px;top:24px;width:44px;height:44px;border-radius:50%;border:2px solid var(--white);display:flex;align-items:center;justify-content:center}
.nl-title{position:absolute;left:238px;top:28px;font-family:'Raleway',sans-serif;font-size:24px;color:var(--white)}
.nl-input{position:absolute;left:512px;top:30px;width:322px;height:34px;background:var(--white);font-size:11px;color:#999;padding:10px 10px}
.nl-btn{position:absolute;left:849px;top:30px;width:163px;height:34px;background:#333;color:var(--white);font-family:'Raleway',sans-serif;font-weight:700;font-size:15px;letter-spacing:.5px;display:flex;align-items:center;justify-content:center}

/* copyright */
.copyright{top:3096px;height:40px;background:var(--darker);color:#bbb;font-size:10.5px}
.copyright .left{position:absolute;left:163px;top:14px}
.copyright .right{position:absolute;right:158px;top:10px;display:flex;align-items:center;gap:6px;font-family:'Raleway',sans-serif;font-weight:700;font-size:11.5px;color:var(--white)}
.card{width:30px;height:19px;background:#e8e8e8;border-radius:2px}
</style>
</head>
<body>

<div class="section topbar">
  <div class="contact">
    <span><svg width="11" height="11" viewBox="0 0 24 24"><path fill="#dfe9f5" d="M6.6 10.8a15 15 0 0 0 6.6 6.6l2.2-2.2c.3-.3.7-.4 1-.2 1.1.4 2.3.6 3.6.6.6 0 1 .4 1 1V20c0 .6-.4 1-1 1A17 17 0 0 1 3 4c0-.6.4-1 1-1h3.5c.6 0 1 .4 1 1 0 1.3.2 2.5.6 3.6.1.3 0 .7-.2 1z"/></svg>Call Us : (555) 014-2290</span>
    <span><svg width="12" height="10" viewBox="0 0 24 18"><rect x="1" y="1" width="22" height="16" fill="none" stroke="#dfe9f5" stroke-width="2"/><path d="M1 1l11 9 11-9" fill="none" stroke="#dfe9f5" stroke-width="2"/></svg>info@reelcoveguide.example</span>
  </div>
  <div class="social"><span class="dot"></span><span class="dot"></span><span class="dot"></span><span class="dot"></span></div>
</div>

<header class="section header">
  <div class="brand"><span class="mark"></span>Dale Marlow</div>
  <nav class="nav">
    <a class="active">Home</a><a>About Us</a><a>Pick Up Location</a><a>Rates</a><a>Contact Us</a><a>Gift Card</a>
  </nav>
</header>

<section class="section hero" role="img" aria-label="Anglers on a charter boat fighting a leaping tarpon on Tampa Bay">
  <div class="badge" role="img" aria-label="Review listing badge"><span class="shape"></span><span class="shape2"></span><span class="circle"></span><span class="bar"></span></div>
  <div class="slide-arrow" style="left:102px"><svg width="10" height="14"><path d="M8 1L2 7l6 6" stroke="#fff" stroke-width="2" fill="none"/></svg></div>
  <div class="slide-arrow" style="left:1054px"><svg width="10" height="14"><path d="M2 1l6 6-6 6" stroke="#fff" stroke-width="2" fill="none"/></svg></div>
  <div class="hero-text">
    <h1>COME FISH WITH TAMPA BAY, FL FISHING GUIDE,</h1>
    <p>Tampa Bay Fishing Charter Most Respected Captain.25 Year Native Guide</p>
  </div>
</section>

<section class="section welcome bubbly">
  <h2>Welcome To <span class="name">Dale Marlow</span></h2>
  <div class="rule"></div>
  <p>Come enjoy a wonderful day fishing charters Tampa for Tarpon, Snook, Redfish, Trout, Sharks, Cobia,Spanish mackerel as well as others aboard Capt. Dale Marlow Sport fishing Charters boat. Capt. Dale will work hard to ensure that you and your guests have a memorable day enjoying the wonderful gamefish that Tampa Bay has to offer.</p>
  <span class="btn">Read More</span>
</section>

<section class="section booking" role="img" aria-label="Angler holding a rod over open water">
  <h3 style="left:161px">Pickup Locations</h3>
  <div class="mini-arrows">
    <span><svg width="7" height="10"><path d="M6 1L2 5l4 4" stroke="#fff" stroke-width="1.5" fill="none"/></svg></span>
    <span><svg width="7" height="10"><path d="M1 1l4 4-4 4" stroke="#fff" stroke-width="1.5" fill="none"/></svg></span>
  </div>
  <h3 style="left:625px">Book Your Day</h3>
  <div class="place-card">
    <h4>HARBOR POINT MARINA</h4>
    <div class="addr">4820 Bayside Road South, Gulf Harbor, FL 33700</div>
    <div class="photo" role="img" aria-label="Aerial view of green islands in turquoise water"></div>
  </div>
  <div class="form-card">
    <div class="form-grid">
      <div class="field"><label>Fast Name</label><div class="input">Name</div></div>
      <div class="field"><label>Phone</label><div class="input">Phone</div></div>
      <div class="field"><label>Email</label><div class="input">Email</div></div>
      <div class="field"><label>Choose Date</label><div class="input">01 / 11 / 2016 <span>▦</span></div></div>
      <div class="field"><label>Choose a Time</label><div class="input">10:00am <span>◷</span></div></div>
      <div class="field"><label>People</label><div class="input">3 <span>⌄</span></div></div>
      <div class="field full"><label>Your Message</label><div class="input area" style="align-items:flex-start">Massage</div></div>
    </div>
    <span class="btn">Book Now</span>
  </div>
</section>

<section class="section rates">
  <h2 class="sec-title">Our <em>Rates</em></h2>
  <div class="rule"></div>
  <div class="side-arrow" style="left:101px"><svg width="8" height="12"><path d="M7 1L2 6l5 5" stroke="#666" stroke-width="1.5" fill="none"/></svg></div>
  <div class="side-arrow" style="left:1054px"><svg width="8" height="12"><path d="M1 1l5 5-5 5" stroke="#666" stroke-width="1.5" fill="none"/></svg></div>
  <div class="rate" style="left:163px">
    <div class="photo" role="img" aria-label="Angler releasing a large tarpon beside the boat" style="background:linear-gradient(160deg,#5a8a6e,#2f6a63 60%,#3d4f4a)"></div>
    <div class="info">
      <h4>Half Day (4 hour) Charter 1-3 people $399, 4 people $499</h4>
      <p>Enjoy a half day trip on the beautiful waters of Tampa Bay. Trip includes all bait, tackle and licenses. Just bring your food and drinks (cooler provided onboard). Recommend you bring sunglasses, hat, and sunscreen.</p>
      <span class="btn">Read More</span>
    </div>
  </div>
  <div class="rate" style="left:627px">
    <div class="photo" role="img" aria-label="Angler on deck holding up a snook" style="background:linear-gradient(160deg,#7f98ad,#4e6b83 55%,#2e3f52)"></div>
    <div class="info">
      <h4>3/4 Day (6 hour) Charter 1-3 people $499, 4 people $599</h4>
      <p>Our most popular and recommended trip.Enjoy a 6 hour trip on the beautiful waters of Tampa Bay. Trip includes all bait, tackle and licenses. Just bring your food and drinks sunglasses, hat, (cooler provided onboard).</p>
      <span class="btn">Read More</span>
    </div>
  </div>
</section>

<section class="section gallery">
  <h2 class="sec-title">Our <em>Gallery</em></h2>
  <div class="rule"></div>
  <svg width="0" height="0" style="position:absolute"><defs><g id="pin"><line x1="76" y1="14" x2="127" y2="14" stroke="#222" stroke-width="2"/><circle cx="76" cy="14" r="4" fill="#222"/><circle cx="127" cy="14" r="4" fill="#222"/></g></defs></svg>

  <div class="tile" style="left:163px;top:110px;height:203px"><svg class="pin"><use href="#pin"/></svg><div class="shot" role="img" aria-label="Anglers landing a fish over green water" style="background:linear-gradient(150deg,#2e8a64,#1f5e4a)"></div></div>
  <div class="tile" style="left:387px;top:110px;height:203px"><svg class="pin"><use href="#pin"/></svg><div class="shot" role="img" aria-label="Two anglers leaning over the gunwale" style="background:linear-gradient(150deg,#6b8d6a,#c7c2b4)"></div></div>
  <div class="tile" style="left:610px;top:110px;height:203px"><svg class="pin"><use href="#pin"/></svg><div class="shot" role="img" aria-label="Anglers holding a catch on a bright day" style="background:linear-gradient(150deg,#b7b8ad,#8c8c80)"></div></div>
  <div class="tile" style="left:834px;top:110px;height:203px"><svg class="pin"><use href="#pin"/></svg><div class="shot" role="img" aria-label="Group showing a big snook on deck" style="background:linear-gradient(150deg,#3d7ea8,#26496a)"></div></div>

  <div class="tile" style="left:163px;top:328px;height:194px"><svg class="pin"><use href="#pin"/></svg><div class="shot" role="img" aria-label="Guide reaching over the side of the boat" style="background:linear-gradient(150deg,#a9b1ad,#5f6f6b)"></div></div>
  <div class="tile" style="left:387px;top:328px;height:194px"><svg class="pin"><use href="#pin"/></svg><div class="shot" role="img" aria-label="Two anglers with a silver tarpon" style="background:linear-gradient(150deg,#4c7a92,#2c4658)"></div></div>
  <div class="tile" style="left:610px;top:328px;height:194px"><svg class="pin"><use href="#pin"/></svg><div class="shot" role="img" aria-label="Fish jumping at night near the boat" style="background:linear-gradient(150deg,#1f3b4b,#0f1f2a)"></div></div>
  <div class="tile" style="left:834px;top:328px;height:194px"><svg class="pin"><use href="#pin"/></svg><div class="shot" role="img" aria-label="Angler holding a snook at dusk" style="background:linear-gradient(150deg,#3c4f61,#1d2a38)"></div></div>
</section>

<section class="section testimonials bubbly">
  <h2 class="sec-title">Client <em>Testimonials</em></h2>
  <div class="rule"></div>
  <span class="qmark" style="left:214px">“</span>
  <span class="qmark" style="left:940px">”</span>
  <p class="quote">Fusce elementum, nulla vel pellentes consequat, ante nulla hendrerit arcu, ac tincidunt mauris lacus sed leo, vamus suscipit molestie vestibulum. Lorem ipsum dolor sit amet, Fusce elementum, nulla vel pellentes consequat, ante nulla hendrerit arcu, ac tincidunt mauris lacus sed leo, vamus suscipit molestie. Fusce elementum, nulla vel</p>
  <div class="client-name">Marisa</div>
  <div class="avatar" role="img" aria-label="Client portrait" style="left:459px"></div>
  <div class="avatar current" role="img" aria-label="Client portrait" style="left:564px"></div>
  <div class="avatar" role="img" aria-label="Client portrait" style="left:668px"></div>
</section>

<footer class="section footer">
  <div class="fcol" style="left:163px">
    <h5>Quick Links</h5>
    <ul><li class="on">Home</li><li>About Us</li><li>Pick Up Locations</li><li>Rates</li><li>Contact Us</li><li>Gift Card</li></ul>
  </div>
  <div class="fcol" style="left:360px">
    <h5>Pickup Locations</h5>
    <ul><li>Harbor Point Marina - Gulf Harbor</li><li>Little Cove - Shoreview</li><li>Rates</li><li>Causeway Boat Ramp</li><li>Pelican Point Ramp</li></ul>
  </div>
  <div class="fcol fcontact" style="left:596px">
    <h5>Contact Info</h5>
    <p style="margin-top:12px"><svg width="12" height="12" viewBox="0 0 24 24"><path fill="#ccc" d="M6.6 10.8a15 15 0 0 0 6.6 6.6l2.2-2.2c.3-.3.7-.4 1-.2 1.1.4 2.3.6 3.6.6.6 0 1 .4 1 1V20c0 .6-.4 1-1 1A17 17 0 0 1 3 4c0-.6.4-1 1-1h3.5c.6 0 1 .4 1 1 0 1.3.2 2.5.6 3.6.1.3 0 .7-.2 1z"/></svg>555-014-2290</p>
    <p><svg width="13" height="10" viewBox="0 0 24 18"><rect x="1" y="1" width="22" height="16" fill="none" stroke="#ccc" stroke-width="2"/><path d="M1 1l11 9 11-9" fill="none" stroke="#ccc" stroke-width="2"/></svg>captain@reelcoveguide.example</p>
    <h5 style="margin-top:14px">Follow Us</h5>
    <div class="fsocial"><span class="dot"></span><span class="dot"></span><span class="dot"></span><span class="dot"></span></div>
  </div>
  <div class="plugin">
    <div class="bar"><span>Recent Activity</span><b>Quillbook</b></div>
    <div class="post"><div class="thumb" role="img" aria-label="Post thumbnail"></div><p>Lorem ipsum dolor sit amet the consectetuer adipis<small>2 people recommended this.</small></p></div>
    <div class="post"><div class="thumb" role="img" aria-label="Post thumbnail"></div><p>Lorem ipsum dolor sit amet the adipiscing elit, sed di nonummy<small>3 people recommended this.</small></p></div>
    <div class="foot">Quillbook social plugin</div>
  </div>
</footer>

<section class="section newsletter">
  <div class="nl-icon"><svg width="20" height="16" viewBox="0 0 24 18"><path d="M1 9L23 1 17 17 11 11z" fill="none" stroke="#fff" stroke-width="2" stroke-linejoin="round"/></svg></div>
  <div class="nl-title">Sign Up For Newsletter</div>
  <div class="nl-input">Enter your email here</div>
  <div class="nl-btn">SUBSCRIBE</div>
</section>

<div class="section copyright">
  <div class="left">Copyright © 2016 by Capt. Dale Marlow. All Rights Reserved</div>
  <div class="right">We Accept <span class="card" style="margin-left:8px"></span><span class="card"></span><span class="card"></span><span class="card"></span></div>
</div>

</body>
</html>
```